Medical Company in need of Modern business card design for new Wound Care clinic.

Modern business card design for our Woundcare company. Logo and description of services can be found on our website; https://www.tornvel-skinheal.com/

```html
<!DOCTYPE html>
<html lang="en">
<head>
<meta charset="utf-8">
<title>Tornvel Skinheal – Business Card</title>
<link rel="stylesheet" href="https://fonts.googleapis.com/css2?family=Poppins:wght@400&family=Raleway:wght@500;700&display=swap">
<style>
  :root {
    --backdrop: #d5d6d8;
    --card-dark: #141414;
    --card-light: #f7f7f7;
    --gold: #c08f35;
    --ink: #151515;
    --shadow: 8px 10px 14px rgba(0,0,0,0.28);
  }
  * { margin: 0; padding: 0; box-sizing: border-box; }
  html, body { width: 900px; height: 1200px; overflow: hidden; background: var(--backdrop); }
  .canvas { position: relative; width: 900px; height: 1200px; }

  .card { position: absolute; left: 133px; width: 633px; height: 364px; box-shadow: var(--shadow); }
  .card--front { top: 210px; background: var(--card-dark); }
  .card--back { top: 624px; background: var(--card-light); }

  .brand-mark {
    position: absolute; left: 50%; width: 16px; height: 16px;
    transform: translateX(-50%); background: var(--gold);
  }
  .card--front .brand-mark { top: 178px; }
  .card--back .brand-mark { top: 70px; }

  .brand-name {
    position: absolute; left: 0; right: 0; text-align: center;
    font-family: 'Poppins', sans-serif; font-weight: 400;
    text-transform: uppercase; white-space: nowrap;
  }
  .card--front .brand-name { top: 214px; font-size: 36px; letter-spacing: 6px; color: var(--gold); }
  .card--back .brand-name { top: 106px; font-size: 27px; letter-spacing: 4.6px; color: var(--ink); }

  .details {
    position: absolute; left: 0; right: 0; text-align: center;
    font-family: 'Raleway', sans-serif; font-weight: 500; color: var(--ink);
  }
  .address { top: 166px; font-size: 15px; }
  .contacts {
    top: 200px; font-size: 15px;
    display: flex; justify-content: center; gap: 22px; align-items: center;
  }
  .contact { display: flex; align-items: center; gap: 5px; }
  .contact svg { width: 14px; height: 14px; fill: var(--gold); }
  .services-title { top: 241px; font-size: 16px; font-weight: 700; color: var(--gold); }
  .services-list { top: 273px; font-size: 14.5px; line-height: 25px; }
  .services-list .sep { font-weight: 700; }
</style>
</head>
<body>
<main class="canvas">
  <section class="card card--front">
    <span class="brand-mark"></span>
    <h1 class="brand-name">Tornvel Skinheal</h1>
  </section>

  <section class="card card--back">
    <span class="brand-mark"></span>
    <h2 class="brand-name">Tornvel Skinheal</h2>

    <p class="details address">4410 Cedar Hollow Rd. Bldg. B, suite 118</p>

    <div class="details contacts">
      <span class="contact">
        <svg viewBox="0 0 24 24"><path d="M6.6 10.8c1.4 2.8 3.8 5.1 6.6 6.6l2.2-2.2c.3-.3.7-.4 1-.2 1.1.4 2.3.6 3.6.6.6 0 1 .4 1 1V20c0 .6-.4 1-1 1C10.6 21 3 13.4 3 4c0-.6.4-1 1-1h3.5c.6 0 1 .4 1 1 0 1.3.2 2.5.6 3.6.1.3 0 .7-.2 1l-2.3 2.2z"/></svg>
        555-014-2386
      </span>
      <span class="contact">
        <svg viewBox="0 0 24 24"><path d="M3 6h4v16H3zM9 3h9l3 3v16H9zM11 10h8v3h-8zm0 5h2v2h-2zm3 0h2v2h-2zm3 0h2v2h-2zm-6 3h2v2h-2zm3 0h2v2h-2zm3 0h2v2h-2z"/></svg>
        555-014-2387
      </span>
      <span class="contact">
        <svg viewBox="0 0 24 24"><path d="M12 2a10 10 0 100 20 10 10 0 000-20zm6.9 6h-3a15 15 0 00-1.3-4A8 8 0 0118.9 8zM12 4c.8 1.2 1.5 2.5 1.9 4h-3.8c.4-1.5 1.1-2.8 1.9-4zM4.3 14a8 8 0 010-4h3.4a16 16 0 000 4zm.8 2h3a15 15 0 001.3 4A8 8 0 015.1 16zm3-8h-3a8 8 0 014.3-4c-.6 1.2-1 2.6-1.3 4zM12 20c-.8-1.2-1.5-2.5-1.9-4h3.8c-.4 1.5-1.1 2.8-1.9 4zm2.3-6H9.7a14 14 0 010-4h4.6a14 14 0 010 4zm.3 6c.6-1.2 1-2.6 1.3-4h3a8 8 0 01-4.3 4zm1.7-6a16 16 0 000-4h3.4a8 8 0 010 4z"/></svg>
        www.tornvel-skinheal.com
      </span>
    </div>

    <h3 class="details services-title">Our Services</h3>
    <p class="details services-list">
      Hyperbaric Oxygen Therapy (HBO): A Cornerstone of Advanced Wound Care<br>
      Debridement <span class="sep">|</span> Advanced Wound Dressings <span class="sep">|</span> Bio-engineered Skin Substitutes<br>
      Compression Therapy and Edema Management
    </p>
  </section>
</main>
</body>
</html>
```